Author needs cover design for health related book

I need the front cover designed for an upcoming book. I want a cover that will stand out when viewed in a thumbnail on sites such as Brindleway. I'm open to the color scheme. The cover design should convey hopeful, uplifting energy, trust, and confidence. Nothing cute or frilly, please. The book is written for newly diagnosed cancer patients. The book title is: They Told Me Today, So What Next? Subtitle: Bravely Facing Cancer Through Worry, Confusion and Dread
Author: Darlisse Hovard
I'm not window shopping. I will definitely pick one of the submitted designs.
Target Market(s)
Newly diagnosed cancer patients
Industry/Entity Type
Health Care
Look and feel
Each slider illustrates characteristics of the customer's brand and the style your logo design should communicate.

```html
<!DOCTYPE html>
<html lang="en">
<head>
<meta charset="utf-8">
<title>They Told Me Today, So What Next? — Book Cover</title>
<link rel="stylesheet" href="https://fonts.googleapis.com/css2?family=Bebas+Neue&family=Oswald:wght@500;700&display=swap">
<style>
  :root {
    --cover-blush: #f1d3da;
    --cover-blush-deep: #ebc3cd;
    --title-charcoal: #4a4a4a;
    --title-magenta: #e2107a;
    --note-yellow: #fbe55a;
    --note-yellow-deep: #f3d640;
    --note-ink: #1d1d1d;
    --pin-red: #d8232a;
    --pin-red-dark: #8f1117;
    --glove-pink: #e98bb6;
    --glove-pale: #f6e3e9;
    --author-ink: #111111;
  }
  * { margin: 0; padding: 0; box-sizing: border-box; }
  html, body {
    width: 886px;
    height: 1200px;
    overflow: hidden;
    background: var(--cover-blush);
  }
  .cover {
    position: relative;
    width: 886px;
    height: 1200px;
    overflow: hidden;
    background: linear-gradient(180deg, var(--cover-blush) 0%, var(--cover-blush-deep) 100%);
  }
  .cover-photo {
    position: absolute;
    left: 0;
    top: 600px;
    width: 886px;
    height: 600px;
    background:
      radial-gradient(ellipse 34% 42% at 30% 52%, var(--glove-pink) 0%, rgba(233,139,182,0.75) 55%, rgba(233,139,182,0) 100%),
      radial-gradient(ellipse 34% 42% at 72% 48%, var(--glove-pink) 0%, rgba(233,139,182,0.75) 55%, rgba(233,139,182,0) 100%),
      linear-gradient(180deg, var(--cover-blush-deep) 0%, var(--glove-pale) 60%, var(--cover-blush) 100%);
  }
  .title {
    position: absolute;
    top: 70px;
    left: 0;
    width: 100%;
    text-align: center;
    font-family: "Bebas Neue", "Oswald", sans-serif;
    line-height: 0.9;
    letter-spacing: 2px;
  }
  .title-line { display: block; }
  .title-line--muted { color: var(--title-charcoal); font-size: 178px; }
  .title-line--accent { color: var(--title-magenta); font-size: 196px; }
  .sticky-note {
    position: absolute;
    left: 170px;
    top: 560px;
    width: 560px;
    height: 200px;
    transform: rotate(-2.5deg);
    background: linear-gradient(160deg, var(--note-yellow) 0%, var(--note-yellow-deep) 100%);
    box-shadow: 0 10px 18px rgba(0,0,0,0.22);
    display: flex;
    align-items: center;
    justify-content: center;
    text-align: center;
    padding: 34px 30px 18px;
  }
  .subtitle {
    font-family: "Oswald", sans-serif;
    font-weight: 500;
    font-size: 33px;
    line-height: 1.22;
    text-transform: uppercase;
    color: var(--note-ink);
  }
  .pushpin {
    position: absolute;
    left: 240px;
    top: -36px;
    width: 56px;
    height: 64px;
  }
  .author {
    position: absolute;
    bottom: 58px;
    left: 0;
    width: 100%;
    text-align: center;
    font-family: "Oswald", sans-serif;
    font-weight: 700;
    font-size: 46px;
    letter-spacing: 0.55em;
    padding-left: 0.55em;
    text-transform: uppercase;
    color: var(--author-ink);
  }
</style>
</head>
<body>
  <main class="cover">
    <div class="cover-photo" role="img" aria-label="Photo of a woman in a white top holding up two pink boxing gloves, a pink awareness ribbon on one glove"></div>

    <h1 class="title">
      <span class="title-line title-line--muted">They Told Me</span>
      <span class="title-line title-line--accent">Today, So</span>
      <span class="title-line title-line--muted">What Next?</span>
    </h1>

    <div class="sticky-note">
      <svg class="pushpin" viewBox="0 0 56 64" aria-hidden="true">
        <line x1="22" y1="40" x2="30" y2="60" stroke="#8a8a8a" stroke-width="3" stroke-linecap="round"/>
        <ellipse cx="26" cy="38" rx="14" ry="6" fill="var(--pin-red-dark)"/>
        <rect x="18" y="18" width="16" height="20" rx="4" fill="var(--pin-red)"/>
        <ellipse cx="26" cy="16" rx="16" ry="10" fill="var(--pin-red)"/>
        <ellipse cx="21" cy="13" rx="5" ry="3" fill="#ff8a8f"/>
      </svg>
      <p class="subtitle">Bravely Facing Cancer<br>Through Worry, Confusion<br>and Dread</p>
    </div>

    <p class="author">Darlisse Hovard</p>
  </main>
</body>
</html>
```